Security doors and flyscreens

We need business cards for our company called K & R Traders. We quote, manufacture and install security doors and flyscreens.

Industry/Entity Type

Security

Contact Information for Business Card

K & R TRADERS
17 Larkfield Ave. Elmwood 3190
Ph: 8127 5506
Fax: 8127 5502
Colin: 0417 952 160
Email: gatemakerhub@mailbox-example.net

```html
<!DOCTYPE html>
<html lang="en">
<head>
<meta charset="utf-8">
<title>K &amp; R Traders – Business Card</title>
<link href="https://fonts.googleapis.com/css2?family=Open+Sans:wght@300;700;800&family=Didact+Gothic&display=swap" rel="stylesheet">
<style>
  :root {
    --bg: #2a2a2a;
    --card: #ffffff;
    --ink: #111111;
    --band: #000000;
    --photo-top: #8a8f86;
    --photo-mid: #a79c92;
    --photo-low: #b8895a;
  }
  * { margin: 0; padding: 0; box-sizing: border-box; }
  html, body { width: 1200px; height: 900px; overflow: hidden; background: var(--bg); }
  .canvas { position: relative; width: 1200px; height: 900px; }
  .card {
    position: absolute; left: 100px; top: 164px;
    width: 1000px; height: 572px;
    background: var(--card);
    overflow: hidden;
  }
  .card__band {
    position: absolute; left: 0; bottom: 0;
    width: 560px; height: 18px; background: var(--band);
  }
  .card__photo {
    position: absolute; top: 0; right: 0;
    width: 440px; height: 100%;
    background: linear-gradient(180deg, var(--photo-top) 0%, var(--photo-mid) 55%, var(--photo-low) 100%);
  }
  .brand {
    position: absolute; top: 58px; left: 0; width: 560px;
    text-align: center; padding-left: 150px;
    font-family: "Open Sans", sans-serif; color: var(--ink);
  }
  .brand__name { font-weight: 800; font-size: 40px; letter-spacing: -1.5px; line-height: 1; }
  .brand__person { font-weight: 300; font-size: 28px; line-height: 1.1; }
  .tagline {
    position: absolute; top: 178px; left: 0; width: 560px;
    padding-left: 150px; text-align: center;
    font-family: "Open Sans", sans-serif; font-weight: 700;
    font-size: 24px; letter-spacing: -0.8px; line-height: 1.35; color: var(--ink);
  }
  .contacts {
    position: absolute; top: 276px; left: 52px;
    list-style: none;
    font-family: "Didact Gothic", sans-serif; font-size: 23px;
    letter-spacing: 3px; color: var(--ink);
  }
  .contacts li { display: flex; align-items: center; height: 46px; }
  .contacts svg { width: 24px; height: 24px; margin-right: 12px; flex: none; }
  .contacts .contacts__email { font-size: 19px; letter-spacing: 1.5px; }
</style>
</head>
<body>
<div class="canvas">
  <div class="card">
    <div class="card__photo" role="img" aria-label="Photo of an installed flyscreen sliding door looking out onto a patio"></div>
    <div class="card__band"></div>

    <div class="brand">
      <div class="brand__name">K &amp; R TRADERS</div>
      <div class="brand__person">Colin</div>
    </div>

    <div class="tagline">manufacture and install<br>security doors and flyscreens</div>

    <ul class="contacts">
      <li>
        <svg viewBox="0 0 24 24"><path d="M12 1a8 8 0 0 0-8 8c0 6 8 14 8 14s8-8 8-14a8 8 0 0 0-8-8zm0 11a3 3 0 1 1 0-6 3 3 0 0 1 0 6z" fill="#111"/></svg>
        17 Larkfield Ave. Elmwood 3190
      </li>
      <li>
        <svg viewBox="0 0 24 24"><path d="M2 8c0-3 4-4 10-4s10 1 10 4v2h-5V8H7v2H2z M5 12h14l2 9H3z" fill="#111"/><circle cx="12" cy="16" r="2.5" fill="#fff"/></svg>
        8127 5506
      </li>
      <li>
        <svg viewBox="0 0 24 24"><rect x="6" y="2" width="12" height="7" fill="#111"/><rect x="2" y="9" width="20" height="9" rx="1.5" fill="#111"/><rect x="6" y="15" width="12" height="7" fill="#fff" stroke="#111" stroke-width="2"/></svg>
        8127 5502
      </li>
      <li>
        <svg viewBox="0 0 24 24"><rect x="2" y="4" width="20" height="16" fill="#111"/><path d="M2 4l10 9 10-9M2 20l8-7M22 20l-8-7" stroke="#fff" stroke-width="1.6" fill="none"/></svg>
        0417 952 160
      </li>
      <li class="contacts__email">
        <svg viewBox="0 0 24 24"><rect x="2" y="3" width="20" height="14" rx="1" fill="none" stroke="#111" stroke-width="2"/><path d="M8 21h8M12 17v4" stroke="#111" stroke-width="2"/></svg>
        gatemakerhub@mailbox-example.net
      </li>
    </ul>
  </div>
</div>
</body>
</html>
```